Tidewell building company Business card design

I need a business card design for my company. I have a logo but dont have business cards with our logo..

www.tidewellbuildingco.com.au

The logo is on the website

I need the same details as this design I have attached. we have changed the logo and colours. just like the website

```html
<!DOCTYPE html>
<html lang="en">
<head>
<meta charset="utf-8">
<title>Tidewell Building – Business Card</title>
<link href="https://fonts.googleapis.com/css2?family=Arimo:wght@400;700&display=swap" rel="stylesheet">
<style>
  :root {
    --page-bg: #4d4d4d;
    --card-blue: #1f8ac6;
    --card-black: #1e1a18;
    --text-white: #ffffff;
    --brand-blue: #2a8fcc;
  }
  * { margin: 0; padding: 0; box-sizing: border-box; }
  html, body {
    width: 1200px;
    height: 1000px;
    overflow: hidden;
    background: var(--page-bg);
    font-family: "Arimo", Arial, sans-serif;
  }
  .business-card {
    position: absolute;
    left: 60px;
    top: 147px;
    width: 1080px;
    height: 706px;
    background: var(--card-blue);
    color: var(--text-white);
    overflow: hidden;
  }
  .card-split {
    position: absolute;
    inset: 0;
    width: 100%;
    height: 100%;
  }
  .brand {
    position: absolute;
    left: 212px;
    top: 150px;
    transform: translateX(-50%);
    display: flex;
    flex-direction: column;
    align-items: center;
    gap: 28px;
  }
  .brand-mark {
    width: 46px;
    height: 46px;
    background: var(--brand-blue);
  }
  .brand-name {
    font-size: 38px;
    font-weight: 400;
    letter-spacing: 3px;
    color: var(--brand-blue);
    text-align: center;
    line-height: 1.15;
    white-space: nowrap;
  }
  .contact-block {
    position: absolute;
    right: 75px;
    text-align: right;
    white-space: nowrap;
  }
  .person-name {
    top: 224px;
    font-size: 41px;
    font-weight: 700;
  }
  .person-role {
    top: 272px;
    font-size: 28px;
  }
  .services {
    top: 420px;
    font-size: 33px;
    line-height: 47px;
  }
  .phones {
    top: 555px;
    font-size: 30px;
  }
  .phones .divider { margin: 0 6px; font-weight: 700; }
  .email {
    top: 612px;
    font-size: 30px;
  }
  .registration {
    position: absolute;
    left: 31px;
    top: 614px;
    font-size: 27px;
  }
</style>
</head>
<body>
  <div class="business-card">
    <svg class="card-split" viewBox="0 0 722 472" preserveAspectRatio="none" aria-hidden="true">
      <polygon points="0,0 469,0 127,472 0,472" fill="var(--card-black)"/>
    </svg>

    <div class="brand">
      <div class="brand-mark"></div>
      <div class="brand-name">Tidewell<br>Building</div>
    </div>

    <div class="contact-block person-name">Marin Dobrescu</div>
    <div class="contact-block person-role">Director</div>

    <div class="contact-block services">
      New Homes - Additions &amp;Renovation<br>
      Domestic &amp; ComercialBuilders
    </div>

    <div class="contact-block phones">0412 555 301<span class="divider">I</span>08 9555 0186</div>
    <div class="contact-block email">tidewellbuildingco@hotmail.com</div>

    <div class="registration">Reg. No. 20583</div>
  </div>
</body>
</html>
```